Visitenkarten-Design für Unternehmensberatung
Zielgruppe
Unternehmensberatung, Auswanderungsberatung und Firmengründung in Dubai. Wir suchen ein modernes Design. unserer Zielgruppe sind deutschsprachige Unternehmer
Aufgabenstellung
Lukas Brandeck - CEO
Adresse: Verano Tech Quarter, Building C7, Dubai, VAE
EMail: info@helvor-plan.de
WhatsApp: +49 1609431772
Mobil: +971 506614372
www.helvor-plan.de
(Instagram: https://www.instagram.com/helvor.plan/)

```html
<!DOCTYPE html>
<html lang="de">
<head>
<meta charset="utf-8">
<title>Helvor Plan – Visitenkarte</title>
<link rel="stylesheet" href="https://fonts.googleapis.com/css2?family=Montserrat:wght@300;400;600;700;800&display=swap">
<style>
  :root {
    --stage: #ececec;
    --card: #ffffff;
    --ink: #2f2f2f;
    --ink-soft: #4a4a4a;
    --band: #3a3a3a;
    --band-text: #f2f2f2;
    --mark-circle: #cdcdcd;
    --shadow: rgba(0, 0, 0, 0.12);
  }
  * { box-sizing: border-box; margin: 0; padding: 0; }
  html, body {
    width: 1200px; height: 719px; overflow: hidden;
    background: var(--stage);
    font-family: "Montserrat", sans-serif;
    color: var(--ink);
  }
  .stage {
    position: relative; width: 1200px; height: 719px;
    display: flex; align-items: center; justify-content: center; gap: 40px;
  }
  .card {
    position: relative; width: 540px; height: 349px;
    background: var(--card);
    box-shadow: 0 10px 28px var(--shadow), 0 2px 6px var(--shadow);
    overflow: hidden;
  }
  .brand { display: flex; align-items: center; gap: 16px; }
  .brand-circle {
    width: 64px; height: 64px; border-radius: 50%;
    background: var(--mark-circle); flex: none;
  }
  .brand-name {
    font-weight: 800; font-size: 30px; letter-spacing: 0.5px;
    color: var(--ink); white-space: nowrap;
  }
  .front .brand { position: absolute; left: 30px; top: 30px; }
  .corner-bar {
    position: absolute; right: 10px; top: 22px;
    width: 7px; height: 42px; background: var(--band);
  }
  .person {
    position: absolute; right: 40px; top: 120px;
    font-size: 22px; white-space: nowrap;
  }
  .person-name { font-weight: 800; }
  .person-role { font-weight: 400; color: var(--ink-soft); }
  .social-band {
    position: absolute; right: 0; top: 162px;
    width: 300px; height: 40px; background: var(--band);
    clip-path: polygon(26px 0, 100% 0, 100% 100%, 0 100%);
    display: flex; align-items: center; justify-content: flex-end;
    gap: 22px; padding-right: 20px;
    color: var(--band-text); font-size: 13px; font-weight: 400;
  }
  .social-item { display: flex; align-items: center; gap: 7px; white-space: nowrap; }
  .social-item svg { width: 15px; height: 15px; flex: none; }
  .contact-list {
    position: absolute; left: 0; bottom: 26px;
    list-style: none; padding-left: 24px;
    border-left: 6px solid var(--band);
  }
  .contact-list li {
    display: flex; align-items: center; gap: 12px;
    font-size: 14px; line-height: 24px; color: var(--ink-soft);
    white-space: nowrap;
  }
  .contact-list svg { width: 15px; height: 15px; flex: none; }
  .back .brand { position: absolute; left: 70px; top: 50%; transform: translateY(-50%); }
  .bottom-bar {
    position: absolute; right: 0; bottom: 0;
    width: 250px; height: 9px; background: var(--band);
  }
</style>
</head>
<body>
<main class="stage">

  <section class="card front" aria-label="Vorderseite">
    <div class="brand">
      <span class="brand-circle"></span>
      <span class="brand-name">HELVOR PLAN</span>
    </div>
    <span class="corner-bar"></span>

    <p class="person"><span class="person-name">LUKAS BRANDECK</span> <span class="person-role">- CEO</span></p>

    <div class="social-band">
      <span class="social-item">
        <svg viewBox="0 0 24 24" fill="none" stroke="currentColor" stroke-width="2" stroke-linecap="round" stroke-linejoin="round"><path d="M5 3h4l2 5-3 2a12 12 0 0 0 6 6l2-3 5 2v4a2 2 0 0 1-2 2A17 17 0 0 1 3 5a2 2 0 0 1 2-2z"/></svg>
        +49 1609431772
      </span>
      <span class="social-item">
        <svg viewBox="0 0 24 24" fill="none" stroke="currentColor" stroke-width="2"><circle cx="12" cy="12" r="9"/></svg>
        @helvor.plan
      </span>
    </div>

    <ul class="contact-list">
      <li>
        <svg viewBox="0 0 24 24" fill="none" stroke="currentColor" stroke-width="2" stroke-linecap="round" stroke-linejoin="round"><path d="M12 22s7-7 7-12a7 7 0 0 0-14 0c0 5 7 12 7 12z"/><circle cx="12" cy="10" r="2.5"/></svg>
        Verano Tech Quarter, Building C7, Dubai, UAE
      </li>
      <li>
        <svg viewBox="0 0 24 24" fill="none" stroke="currentColor" stroke-width="2" stroke-linecap="round" stroke-linejoin="round"><path d="M5 3h4l2 5-3 2a12 12 0 0 0 6 6l2-3 5 2v4a2 2 0 0 1-2 2A17 17 0 0 1 3 5a2 2 0 0 1 2-2z"/></svg>
        +971 506614372
      </li>
      <li>
        <svg viewBox="0 0 24 24" fill="none" stroke="currentColor" stroke-width="2" stroke-linejoin="round"><rect x="3" y="5" width="18" height="14" rx="1"/><path d="M3 6l9 7 9-7"/></svg>
        info@helvor-plan.de
      </li>
      <li>
        <svg viewBox="0 0 24 24" fill="none" stroke="currentColor" stroke-width="2"><circle cx="12" cy="12" r="9"/><path d="M3 12h18M12 3c3 3 3 15 0 18M12 3c-3 3-3 15 0 18"/></svg>
        www.helvor-plan.de
      </li>
    </ul>
  </section>

  <section class="card back" aria-label="Rückseite">
    <div class="brand">
      <span class="brand-circle"></span>
      <span class="brand-name">HELVOR PLAN</span>
    </div>
    <span class="bottom-bar"></span>
  </section>

</main>
</body>
</html>
```